KAY VELORE

We need a letterhead design for an Image & Etiquette Consultancy company based in Singapore.

The services we provide are Personal Image Consultation, Image & Etiquette Workshop for schools and corporate.

The design should have our corporate colour as seen in the logo files I have uploaded.

Since our company helps clients with their image, the design should be aesthetically very appealing. It should reflect a very classy & elegant feel.

I will print the letterhead using my printer but most of the time will use it to write letters to my clients therefore the format should include MS Word.

```html
<!DOCTYPE html>
<html lang="en">
<head>
<meta charset="utf-8">
<title>Kay Velore Letterhead</title>
<link rel="stylesheet" href="https://fonts.googleapis.com/css2?family=Open+Sans:wght@300;400;600;700&display=swap">
<style>
  :root {
    --backdrop: #c9ced1;
    --paper: #ffffff;
    --indigo: #2a1682;
    --indigo-deep: #1f0f6b;
    --violet-soft: #4a2aa8;
    --gold: #c9a24a;
    --ink: #111111;
    --muted: #8a8a8a;
    --footer-mark: #b9b9c6;
  }
  * { box-sizing: border-box; margin: 0; padding: 0; }
  html, body { width: 1200px; height: 1200px; overflow: hidden; }
  body {
    background: var(--backdrop);
    font-family: "Open Sans", Arial, sans-serif;
    position: relative;
  }
  .letterhead {
    position: absolute;
    left: 220px;
    top: 62px;
    width: 760px;
    height: 1076px;
    background: var(--paper);
    overflow: hidden;
  }
  .header-band { position: absolute; left: 0; top: 0; width: 760px; height: 180px; }
  .header-decoration {
    position: absolute;
    left: 240px;
    top: 22px;
    width: 330px;
    height: 86px;
    background: linear-gradient(90deg, var(--indigo) 0%, var(--violet-soft) 50%, var(--indigo) 100%);
  }
  .brand {
    position: absolute;
    left: 36px;
    top: 38px;
    color: var(--gold);
  }
  .brand-name {
    font-weight: 300;
    font-size: 30px;
    letter-spacing: 2px;
    line-height: 1;
  }
  .brand-tagline {
    font-weight: 300;
    font-size: 8px;
    letter-spacing: 1.5px;
    text-transform: uppercase;
    margin-top: 5px;
  }
  .letter-body {
    position: absolute;
    left: 110px;
    top: 300px;
    width: 560px;
  }
  .letter-title {
    font-weight: 700;
    font-size: 24px;
    color: var(--ink);
    margin-bottom: 58px;
  }
  .letter-paragraph {
    font-size: 10.5px;
    line-height: 1.5;
    text-transform: uppercase;
    text-align: justify;
    color: var(--ink);
    margin-bottom: 22px;
  }
  .signature {
    position: absolute;
    left: 110px;
    top: 740px;
  }
  .signature-name {
    font-weight: 700;
    font-size: 26px;
    color: var(--ink);
    margin-bottom: 4px;
  }
  .signature-line {
    font-size: 11px;
    color: var(--muted);
    line-height: 1.5;
  }
  .footer-band {
    position: absolute;
    left: 0;
    bottom: 0;
    width: 760px;
    height: 64px;
    background: var(--indigo);
  }
  .footer-brand {
    position: absolute;
    right: 22px;
    bottom: 12px;
    text-align: right;
    color: var(--footer-mark);
  }
  .footer-brand-name {
    font-weight: 300;
    font-size: 15px;
    letter-spacing: 1px;
    line-height: 1;
  }
  .footer-brand-tagline {
    font-weight: 300;
    font-size: 5px;
    letter-spacing: 1px;
    text-transform: uppercase;
    margin-top: 2px;
  }
</style>
</head>
<body>
  <main class="letterhead">
    <svg class="header-band" viewBox="0 0 760 180" aria-hidden="true">
      <polygon points="0,0 560,0 629,120 0,120" fill="var(--indigo)"/>
      <polygon points="600,0 760,0 760,175 700,175" fill="var(--indigo-deep)"/>
    </svg>
    <div class="header-decoration" role="img" aria-label="Decorative header artwork area"></div>

    <div class="brand">
      <div class="brand-name">KAY VELORE</div>
      <div class="brand-tagline">Image &amp; Etiquette Consultancy</div>
    </div>

    <section class="letter-body">
      <h1 class="letter-title">About Our Company</h1>
      <p class="letter-paragraph">Kay Velore is an image and etiquette consultancy based in Singapore. We help individuals and organisations present themselves with confidence, poise and quiet elegance. Our consultants bring years of experience in styling, grooming, communication and professional conduct, and every programme is tailored to the goals of each client we serve.</p>
      <p class="letter-paragraph">Our personal image consultation covers wardrobe planning, colour analysis, grooming and body language. Each session is private and unhurried, leaving you with clear guidance and a look that feels entirely your own. Follow-up reviews help you keep the results long after our time together ends.</p>
      <p class="letter-paragraph">We also run image and etiquette workshops for schools and corporate teams. Students learn dining manners, courtesy and self-presentation, while professionals refine business etiquette, meeting conduct and client care. Workshops can be held at your premises or at our studio, in half-day or full-day formats, and each one closes with practical exercises and a personal takeaway guide for every participant.</p>
    </section>

    <section class="signature">
      <div class="signature-name">ELISE TAN</div>
      <div class="signature-line">Senior Editor</div>
      <div class="signature-line">555 014 2290</div>
      <div class="signature-line">hello@kayvelore.sg</div>
    </section>

    <footer class="footer-band">
      <div class="footer-brand">
        <div class="footer-brand-name">KAY VELORE</div>
        <div class="footer-brand-tagline">Image &amp; Etiquette Consultancy</div>
      </div>
    </footer>
  </main>
</body>
</html>
```